National Virtual accounting firm needs website designed

I need a wordpress website design for a national virtual accounting firm. I will upload my business card, logo, and postcards that I have had designed and followed the same style. I want a similar style to be followed so I can keep the running theme similar.

Services include:

Tax Services:
Tax preparation and planning services for Individuals, businesses, estates, and nonprofits
Full Service Payroll for Businesses
QVT Audit Representation

Consulting:
Entity Selection & Restructuring
Financial Projections & Forecasts
Retirement Planning
IPO Readiness

Accounting:
Bookkeeping
Reviews and Compilations
Payroll Services

Other Services:
CFO Services
Compliance Services
Controller Services
Software Implementations for Tenvolk, Brombalt, and Plovena.

Target Market(s)

small to medium size businesses, and individuals

Industry/Entity Type

accounting firms

Font styles to use
Sans Serif

Colors
59FF00
82FF00
B8FF75
E3FFCB
F4FFEA

Requirements
Must have
• Color schematics from the logo and post cards/business cards

```html
<!DOCTYPE html>
<html lang="en">
<head>
<meta charset="utf-8">
<title>Verdano – Virtual Accounting</title>
<link rel="stylesheet" href="https://fonts.googleapis.com/css2?family=Merriweather:wght@400;700;900&display=swap">
<style>
:root{
  --green:#3fae2a;
  --green-light:#8cc63f;
  --green-dark:#137a3a;
  --lime:#59c219;
  --yellow:#f7c600;
  --ink:#1c1c1c;
  --text:#3a3a3a;
  --night:#0e1a1c;
  --mist:#f1f4f3;
  --white:#ffffff;
}
*{margin:0;padding:0;box-sizing:border-box}
html,body{width:1200px;height:4508px;overflow:hidden}
body{position:relative;font-family:"Merriweather",Georgia,serif;color:var(--text);background:var(--white)}
.abs{position:absolute}
.wave{position:absolute;left:0;width:1200px;display:block}

/* header */
.site-header{position:absolute;top:0;left:0;width:1200px;height:115px;background:var(--white);z-index:5}
.brand{position:absolute;display:flex;align-items:center;gap:10px;font-weight:900;color:var(--ink)}
.brand-dot{width:22px;height:22px;border-radius:50%;background:var(--yellow)}
.header-brand{left:128px;top:30px;font-size:40px}
.header-phone{position:absolute;left:604px;top:14px;font-size:18px;font-weight:700;color:var(--ink)}
.consult-btn{position:absolute;left:780px;top:0;width:312px;height:50px;background:var(--green-light);color:var(--white);border-radius:0 0 26px 26px;font-size:14px;font-weight:700;display:flex;align-items:center;justify-content:center}
.main-nav{position:absolute;left:487px;top:73px;display:flex;gap:26px;font-size:14px;font-weight:700;color:var(--ink)}

/* hero */
.hero{position:absolute;top:115px;left:0;width:1200px;height:770px;background:var(--night);overflow:hidden}
.hero-photo{position:absolute;left:420px;top:0;width:780px;height:770px;background:linear-gradient(90deg,#0e1a1c 0%,#3a4648 30%,#8a9496 60%,#c9d0d2 100%)}
.hero-title{position:absolute;left:126px;top:150px;font-size:47px;line-height:53px;font-weight:700;color:var(--white);width:420px}
.hero-title span{color:var(--lime)}
.pill{position:absolute;border-radius:30px;background:var(--yellow);color:var(--ink);font-weight:700;display:flex;align-items:center;justify-content:center}
.hero-btn{left:126px;top:505px;width:236px;height:56px;font-size:21px}

/* about */
.about-ring{position:absolute;left:128px;top:900px;width:414px;height:396px;border:3px solid var(--green);border-radius:50%}
.about-photo{position:absolute;left:150px;top:918px;width:370px;height:360px;border-radius:50%;background:radial-gradient(circle at 40% 40%,#c7d3e0,#6d7f93 60%,#3b4656)}
h2.section-title{position:absolute;font-size:40px;font-weight:900;color:var(--ink);letter-spacing:.5px}
.about-title{left:578px;top:922px}
.about-text{position:absolute;left:580px;top:988px;width:470px;font-size:16px;line-height:22.5px}
.about-btn{left:582px;top:1212px;width:152px;height:46px;font-size:16px}

/* services */
.mist{position:absolute;left:0;top:1360px;width:1200px;height:650px;background:var(--mist)}
.center{left:0;width:1200px;text-align:center}
.lede{position:absolute;left:0;width:1200px;text-align:center;font-size:16px;line-height:23px}
.tabs{position:absolute;left:128px;top:1610px;width:944px;height:144px;border-bottom:2px solid #d6d9d8}
.tab{position:absolute;top:0;width:200px;text-align:center;font-size:24px;color:var(--ink)}
.tab svg{display:block;margin:0 auto 14px}
.tab.active::after{content:"";position:absolute;left:4px;right:4px;top:140px;height:5px;background:var(--green)}
.service-card{position:absolute;left:128px;top:1800px;width:944px;height:380px;background:var(--white);border-radius:40px;box-shadow:0 6px 30px rgba(0,0,0,.08)}
.service-photo{position:absolute;left:37px;top:28px;width:353px;height:317px;border-radius:40px;background:linear-gradient(135deg,#2e3a44,#7b8a96 55%,#c08a4a)}
.service-title{position:absolute;left:437px;top:52px;font-size:33px;color:var(--ink)}
.service-text{position:absolute;left:437px;top:106px;width:460px;font-size:16px;line-height:22.5px}
.ticks{position:absolute;left:437px;top:190px;width:460px;list-style:none;font-size:16px;font-weight:700;color:var(--ink);line-height:22.5px}
.ticks li{position:relative;padding-left:25px;margin-bottom:12px}
.ticks li::before{content:"";position:absolute;left:0;top:6px;width:13px;height:13px;border-radius:50%;background:var(--yellow);box-shadow:inset 0 0 0 3px var(--green)}

/* why */
.why{position:absolute;left:0;top:2300px;width:1200px;height:438px;background:linear-gradient(180deg,#46ac3a,var(--green-dark))}
.why-item{position:absolute;top:2535px;width:220px;text-align:center;color:var(--white);font-size:24px;font-weight:700}
.why-item svg{display:block;margin:0 auto 18px}

/* blog */
.post{position:absolute;top:2985px;width:288px;height:380px;border:1px solid #e1e4e3;border-radius:8px;overflow:hidden;background:var(--white);text-align:center}
.post-photo{height:190px}
.post h3{font-size:17px;line-height:20px;color:var(--ink);margin:35px 30px 12px}
.post p{font-size:14px;line-height:17px;margin:0 28px}
.post time{display:block;margin-top:14px;font-size:14px;font-weight:700;color:var(--green)}

/* contact */
.contact-title{position:absolute;left:131px;top:3650px;font-size:42px;font-weight:400;color:var(--white)}
.contact-text{position:absolute;left:131px;top:3725px;width:440px;font-size:16px;line-height:22.5px;color:#f4ffea}
.field{position:absolute;left:684px;width:367px;height:46px;background:var(--white);border:none;font-family:inherit;font-size:14px;color:#777;padding:14px}
.field.msg{height:122px}
.submit{position:absolute;left:784px;top:3890px;width:136px;height:50px;border-radius:25px;background:#0a0a0a;color:var(--white);font-weight:700;font-size:16px;display:flex;align-items:center;justify-content:center}

/* footer */
.footer{position:absolute;left:0;top:4040px;width:1200px;height:468px;background:var(--night)}
.foot-head{position:absolute;top:4140px;font-size:27px;color:var(--yellow);font-weight:400}
.foot-links{position:absolute;top:4202px;list-style:none;font-size:16px;line-height:29px;color:var(--white)}
.footer-brand{left:460px;top:4162px;font-size:42px;color:var(--white)}
.foot-blurb{position:absolute;left:440px;top:4256px;width:320px;text-align:center;font-size:16px;line-height:23px;color:var(--white)}
.foot-contact{position:absolute;left:826px;top:4202px;list-style:none;font-size:16px;line-height:20px;color:var(--white)}
.foot-contact li{display:flex;gap:12px;margin-bottom:18px}
.foot-contact svg{flex:none;margin-top:2px}
.rule{position:absolute;left:0;top:4400px;width:1200px;height:1px;background:#26343a}
.copyright{position:absolute;left:127px;top:4450px;font-size:16px;color:var(--white)}
.social{position:absolute;top:4440px;width:38px;height:38px;border-radius:50%;background:var(--green-light)}
</style>
</head>
<body>

<header class="site-header">
  <div class="brand header-brand"><span class="brand-dot"></span>Verdano</div>
  <div class="header-phone">(555) 014-2290</div>
  <div class="consult-btn">Schedule a free Consult now</div>
  <nav class="main-nav"><span>HOME</span><span>ABOUT</span><span>SERVICES</span><span>NEWS</span><span>WHY CHOOSE US</span><span>CONTACT</span></nav>
</header>

<section class="hero">
  <div class="hero-photo" role="img" aria-label="Smiling advisor in a grey suit shaking hands with a client in an office"></div>
  <h1 class="hero-title">Why Settle for less when your Finances could be <span>EXACT?</span></h1>
  <div class="pill hero-btn">Get Started Here</div>
</section>
<svg class="wave" style="top:760px" height="130" viewBox="0 0 1200 130" preserveAspectRatio="none">
  <path d="M0 70 Q600 -10 1200 40 L1200 130 L0 130Z" fill="#8cc63f"/>
  <path d="M0 125 Q500 30 1200 85 L1200 130 L0 130Z" fill="#3fae2a"/>
  <path d="M0 125 Q600 55 1200 100 L1200 130 L0 130Z" fill="#ffffff"/>
</svg>

<section class="about">
  <div class="about-ring"></div>
  <div class="about-photo" role="img" aria-label="Team reviewing financial charts and a calculator at a desk"></div>
  <h2 class="section-title about-title">ABOUT US</h2>
  <p class="about-text">Lorem ipsum dolor sit amet, consectetur adipiscing elit, sed do eiusmod tempor incididunt ut labore et dolore magna aliqua. Quis ipsum suspendisse ultrices gravida. Risus commodo viverra maecenas accumsan lacus vel facilisis.Lorem ipsum dolor sit amet, consectetur adi piscing elit, sed do eiusmod tempor incididunt ut labore et dolore magna aliqua. Quis ipsum suspendisse ultrices gravida. Risus commodo viverra maecenas accumsan lacus vel facilisis.</p>
  <div class="pill about-btn">Read More</div>
</section>

<svg class="wave" style="top:1300px" height="62" viewBox="0 0 1200 62" preserveAspectRatio="none">
  <path d="M0 0 Q600 120 1200 0 L1200 62 L0 62Z" fill="#f1f4f3"/>
</svg>
<div class="mist"></div>

<section class="services">
  <h2 class="section-title center" style="top:1475px">OUR SERVICES</h2>
  <p class="lede" style="top:1540px">Lorem ipsum dolor sit amet, consectetur adipiscing elit, sed do eiusmod tempor<br>incididunt ut labore et dolore magna aliqua. Quis ipsum suspendisse ultrices.</p>
  <div class="tabs">
    <div class="tab active" style="left:26px">
      <svg width="70" height="74" viewBox="0 0 70 74" fill="none" stroke="#3fae2a" stroke-width="2.5"><path d="M14 4h32l12 12v54H14z"/><path d="M24 24h24M24 34h24M24 44h14"/><circle cx="18" cy="58" r="10" fill="#fff"/><path d="M13 58l4 4 7-8"/></svg>
      Tax Services</div>
    <div class="tab" style="left:258px">
      <svg width="70" height="74" viewBox="0 0 70 74" fill="none" stroke="#3fae2a" stroke-width="2.5"><circle cx="35" cy="16" r="8"/><path d="M22 44c0-10 6-16 13-16s13 6 13 16"/><path d="M8 48h54M14 48v22M56 48v22"/><rect x="42" y="4" width="20" height="14"/></svg>
      Consulting</div>
    <div class="tab" style="left:471px">
      <svg width="70" height="74" viewBox="0 0 70 74" fill="none" stroke="#3fae2a" stroke-width="2.5"><rect x="8" y="4" width="34" height="46" rx="3"/><path d="M14 12h22M14 22h6M24 22h6M14 32h6M24 32h6"/><path d="M28 40h34v30H28z"/><circle cx="45" cy="55" r="8"/><path d="M45 50v10"/></svg>
      Accounting</div>
    <div class="tab" style="left:707px">
      <svg width="70" height="74" viewBox="0 0 70 74" fill="none" stroke="#3fae2a" stroke-width="2.5"><rect x="8" y="8" width="40" height="60" rx="3"/><path d="M20 4h16v8H20zM16 26h22M16 36h22M16 46h12"/><path d="M48 34l14 6v12c0 8-6 13-14 16-8-3-14-8-14-16V40z"/><path d="M42 52l5 5 8-9"/></svg>
      Other Services</div>
  </div>

  <article class="service-card">
    <div class="service-photo" role="img" aria-label="Hands typing on a laptop with floating tax and finance icons"></div>
    <h3 class="service-title">Tax Services:</h3>
    <p class="service-text">Lorem ipsum dolor sit amet, consectetur adipiscing elit, sed do eiusmod dolor sit amet, consectetur adipiscing elit, sed do eiusmod tempor incididunt.</p>
    <ul class="ticks">
      <li>Tax preparation and planning services for Individuals, businesses, estates, and nonprofits</li>
      <li>Full Service Payroll for Businesses</li>
      <li>QVT Audit Representation</li>
    </ul>
  </article>
</section>

<svg class="wave" style="top:2210px" height="95" viewBox="0 0 1200 95" preserveAspectRatio="none">
  <path d="M0 0 Q500 150 1200 20 L1200 95 L0 95Z" fill="#46ac3a"/>
  <path d="M0 0 Q520 140 1200 35 L1200 95 L0 95Z" fill="#8cc63f" opacity=".0"/>
</svg>
<section class="why">
</section>
<h2 class="section-title center" style="top:2390px;color:#fff;font-size:38px">WHY CHOOSE US?</h2>
<p class="lede" style="top:2452px;color:#fff">Lorem ipsum dolor sit amet, consectetur adipiscing elit, sed do eiusmod tempor<br>incididunt ut labore et dolore magna aliqua. Quis ipsum suspendisse ultrices.</p>
<div class="why-item" style="left:262px">
  <svg width="90" height="90" viewBox="0 0 90 90" fill="none" stroke="#f7c600" stroke-width="2.5"><circle cx="32" cy="28" r="18" stroke-dasharray="6 3"/><circle cx="32" cy="28" r="9"/><path d="M12 80c0-14 8-22 20-22s20 8 20 22"/><circle cx="66" cy="50" r="14"/><path d="M66 42v8l6 4"/></svg>
  Expirienced</div>
<div class="why-item" style="left:490px">
  <svg width="90" height="90" viewBox="0 0 90 90" fill="none" stroke="#f7c600" stroke-width="2.5"><circle cx="45" cy="30" r="26" stroke-dasharray="3 4"/><circle cx="33" cy="24" r="5"/><circle cx="45" cy="22" r="5"/><circle cx="57" cy="24" r="5"/><path d="M25 40c0-6 4-9 8-9M37 38c0-6 4-9 8-9s8 3 8 9M57 31c4 0 8 3 8 9"/><path d="M6 62h14v22H6zM20 66h22l24-8c6-2 8 4 4 6L44 78H20"/></svg>
  Profesional</div>
<div class="why-item" style="left:705px">
  <svg width="90" height="90" viewBox="0 0 90 90" fill="none" stroke="#f7c600" stroke-width="2.5"><circle cx="50" cy="26" r="20"/><path d="M56 18c-2-3-12-3-12 3s12 4 12 10-10 6-13 2M50 12v30"/><path d="M6 62h14v22H6zM20 66h22l24-8c6-2 8 4 4 6L44 78H20"/></svg>
  Afordable</div>

<section class="blog">
  <h2 class="section-title center" style="top:2835px">LATEST BLOG POSTS</h2>
  <p class="lede" style="top:2900px">Lorem ipsum dolor sit amet, consectetur adipiscing elit, sed do eiusmod tempor<br>incididunt ut labore et dolore magna aliqua. Quis ipsum suspendisse ultrices.</p>
  <article class="post" style="left:128px">
    <div class="post-photo" role="img" aria-label="Hand writing beside a calculator and glasses on paperwork" style="background:linear-gradient(135deg,#8a6a4a,#d8c9b4 60%,#f1ece4)"></div>
    <h3>Lorem ipsum dolor sit am etconse ctetore.</h3>
    <p>Lorem ipsum dolor sit ametco nectetur adipiscing elit, sedod olor eiusmod tempor.</p>
    <time>June 17 2023</time>
  </article>
  <article class="post" style="left:456px">
    <div class="post-photo" role="img" aria-label="Colleagues discussing work at a computer in an office" style="background:linear-gradient(135deg,#c9cbcc,#8a6a44 50%,#2d2a28)"></div>
    <h3>Lorem ipsum dolor sit am etconse ctetore.</h3>
    <p>Lorem ipsum dolor sit ametco nectetur adipiscing elit, sedod olor eiusmod tempor.</p>
    <time>June 17 2023</time>
  </article>
  <article class="post" style="left:784px">
    <div class="post-photo" role="img" aria-label="Team pointing at printed reports on a meeting table" style="background:linear-gradient(135deg,#5a6d80,#c8d0d8 55%,#eef1f4)"></div>
    <h3>Lorem ipsum dolor sit am etconse ctetore.</h3>
    <p>Lorem ipsum dolor sit ametco nectetur adipiscing elit, sedod olor eiusmod tempor.</p>
    <time>June 17 2023</time>
  </article>
</section>

<svg class="wave" style="top:3440px" height="620" viewBox="0 0 1200 620" preserveAspectRatio="none">
  <defs><linearGradient id="contactFill" x1="0" y1="0" x2="1" y2="1"><stop offset="0" stop-color="#5cbf2a"/><stop offset="1" stop-color="#3aa52c"/></linearGradient></defs>
  <path d="M0 120 Q600 -60 1200 40 L1200 620 L0 620Z" fill="#2f9e2c"/>
  <path d="M0 130 Q600 -30 1200 60 L1200 560 Q600 500 0 590Z" fill="url(#contactFill)"/>
  <path d="M0 600 Q600 470 1200 540 L1200 620 L0 620Z" fill="#8cc63f"/>
</svg>
<div class="footer"></div>
<svg class="wave" style="top:4010px" height="60" viewBox="0 0 1200 60" preserveAspectRatio="none">
  <path d="M0 40 Q600 -20 1200 20 L1200 60 L0 60Z" fill="#0e1a1c"/>
</svg>

<section class="contact">
  <h2 class="contact-title">Contact Us</h2>
  <p class="contact-text">Lorem ipsum dolor sit amet, consectetur adipiscing elit, sed do eiusmod tempor incididunt ut labore et dolore magna aliqua. Quis ipsum suspendisse ultrices gravida. Risus commodo viverra maecenas accumsan lacus vel facilisis.</p>
  <div class="field" style="top:3613px">Name:</div>
  <div class="field" style="top:3673px">Phone:</div>
  <div class="field" style="top:3733px">Email:</div>
  <div class="field msg" style="top:3793px">Message:</div>
  <div class="submit">SUBMIT</div>
</section>

<footer>
  <h4 class="foot-head" style="left:125px">Menu</h4>
  <ul class="foot-links" style="left:127px"><li>Home</li><li>About Us</li><li>Services</li><li>News</li><li>Why Us</li></ul>
  <ul class="foot-links" style="left:245px"><li>Tax Services</li><li>Consulting</li><li>Accounting</li><li>Other Services</li></ul>
  <div class="brand footer-brand"><span class="brand-dot"></span>Verdano</div>
  <p class="foot-blurb">Lorem ipsum dolor sit amet, consectetur adipiscing elit, sed do eiusmod tempor incididunt</p>
  <h4 class="foot-head" style="left:826px">Contact</h4>
  <ul class="foot-contact">
    <li><svg width="14" height="18" viewBox="0 0 14 18"><path d="M7 0a7 7 0 0 0-7 7c0 5 7 11 7 11s7-6 7-11a7 7 0 0 0-7-7z" fill="#8cc63f"/><circle cx="7" cy="7" r="2.5" fill="#0e1a1c"/></svg><span>Dummy Addres 231<br>Street name Lorem ipsum.</span></li>
    <li><svg width="16" height="16" viewBox="0 0 16 16"><path d="M3 1l3 3-2 2c1 2 3 4 5 5l2-2 3 3-2 3C6 15 1 10 1 3z" fill="#8cc63f"/></svg><span>Phone: (555) 014-2290</span></li>
    <li><svg width="16" height="16" viewBox="0 0 16 16"><rect x="1" y="5" width="14" height="10" fill="#8cc63f"/><rect x="4" y="1" width="8" height="5" fill="#8cc63f"/></svg><span>Fax: 555-013-7741</span></li>
    <li><svg width="16" height="16" viewBox="0 0 16 16"><rect x="1" y="3" width="14" height="10" fill="#8cc63f"/><path d="M1 3l7 6 7-6" stroke="#0e1a1c" fill="none"/></svg><span>info@verdano.example</span></li>
  </ul>
  <div class="rule"></div>
  <p class="copyright">Copyright&nbsp; 2023 © All Rights Reserved.</p>
  <span class="social" style="left:991px"></span>
  <span class="social" style="left:1039px"></span>
</footer>

</body>
</html>
```